Astrologer needs a design for business card

I need a business card design for my job in astrology and flower therapy.
In front side need the information add file.

In back side need the informations above:
INTERPRETAÇÕES
TENDÊNCIAS
AUTOCONHECIMENTO
ANÁLISE VOCACIONAL
DIRECIONAMENTO DE CARREIRA
RELACIONAMENTOS
ASTROLOGIA EMPRESARIAL
TERAPIA FLORAL – Florias de Dorsk e Rui Tavenco

Business

OVRA

```html
<!DOCTYPE html>
<html lang="pt">
<head>
<meta charset="utf-8">
<title>Liora Venn – Cartão de visita</title>
<link rel="stylesheet" href="https://fonts.googleapis.com/css2?family=Arimo:wght@400;700&family=Marcellus&display=swap">
<style>
  :root {
    --page-bg: #e9e7ec;
    --card-bg: #7f7589;
    --card-ink: #d3cae2;
    --card-ink-soft: #c4bad3;
    --pattern-tone-a: #8a7f96;
    --pattern-tone-b: #a79cba;
    --rule: #b3a9c2;
  }
  * { box-sizing: border-box; margin: 0; padding: 0; }
  html, body { width: 1200px; height: 900px; overflow: hidden; }
  body {
    background: var(--page-bg);
    position: relative;
    font-family: "Arimo", Arial, sans-serif;
  }
  .card {
    position: absolute;
    top: 276px;
    width: 525px;
    height: 348px;
    background: var(--card-bg);
    box-shadow: 0 6px 18px rgba(40, 30, 50, 0.25);
    overflow: hidden;
  }
  .card--front { left: 50px; }
  .card--back { left: 625px; }

  .zodiac-pattern {
    position: absolute;
    inset: 0;
    background:
      radial-gradient(circle at 20% 25%, var(--pattern-tone-b) 0, transparent 22%),
      radial-gradient(circle at 55% 50%, var(--pattern-tone-b) 0, transparent 24%),
      radial-gradient(circle at 85% 78%, var(--pattern-tone-b) 0, transparent 22%),
      linear-gradient(135deg, var(--pattern-tone-a), var(--card-bg));
    opacity: 0.9;
  }

  .identity {
    position: absolute;
    left: 42px;
    top: 82px;
    color: var(--card-ink);
    font-weight: 700;
    line-height: 0.9;
  }
  .identity__first { font-size: 44px; letter-spacing: -0.5px; display: block; }
  .identity__last { font-size: 22px; display: block; margin-top: 2px; padding-left: 2px; }

  .contact {
    position: absolute;
    left: 275px;
    top: 105px;
    color: var(--card-ink);
    font-weight: 400;
  }
  .contact__row { display: flex; align-items: center; gap: 8px; }
  .contact__row--phone { font-size: 19px; }
  .contact__row--mail { font-size: 14px; margin-top: 6px; color: var(--card-ink-soft); }
  .contact svg { flex: none; }

  .services {
    position: absolute;
    left: 18px;
    right: 14px;
    top: 250px;
    font-family: "Marcellus", Georgia, serif;
    color: var(--card-ink);
    text-transform: uppercase;
  }
  .services__grid {
    display: grid;
    grid-template-columns: 176px 124px 1fr;
  }
  .services__col {
    padding: 0 6px;
    line-height: 1.05;
  }
  .services__col + .services__col { border-left: 1px solid var(--rule); }
  .services__col--one, .services__col--two { text-align: right; }
  .services__col--three { text-align: center; }
  .services__head { font-size: 17px; }
  .services__sub { font-size: 12px; }
  .services__col--three .services__sub { font-size: 12px; }
  .services__col--three .services__sub--large { font-size: 15px; }
  .services__floral {
    font-size: 12px;
    text-align: right;
    width: 300px;
    margin-top: -1px;
    padding-right: 6px;
  }
  .services__floral span { text-transform: none; }
</style>
</head>
<body>

  <section class="card card--front" aria-label="Frente do cartão">
    <div class="zodiac-pattern" role="img" aria-label="Padrão com as ilustrações dos doze signos do zodíaco em lilás claro"></div>
  </section>

  <section class="card card--back" aria-label="Verso do cartão">
    <h1 class="identity">
      <span class="identity__first">Liora</span>
      <span class="identity__last">Venn</span>
    </h1>

    <div class="contact">
      <div class="contact__row contact__row--phone">
        <svg width="11" height="17" viewBox="0 0 11 17" aria-hidden="true">
          <rect x="1" y="1" width="9" height="15" rx="1.5" fill="none" stroke="currentColor" stroke-width="1.4"/>
          <line x1="4" y1="13.5" x2="7" y2="13.5" stroke="currentColor" stroke-width="1.2"/>
        </svg>
        <span>(51) 9284-0617</span>
      </div>
      <div class="contact__row contact__row--mail">
        <svg width="14" height="10" viewBox="0 0 14 10" aria-hidden="true">
          <rect x="0.5" y="0.5" width="13" height="9" fill="currentColor"/>
          <polyline points="0.5,0.5 7,5.5 13.5,0.5" fill="none" stroke="#7f7589" stroke-width="1"/>
        </svg>
        <span>lioravenn@mailbox.com</span>
      </div>
    </div>

    <div class="services">
      <div class="services__grid">
        <div class="services__col services__col--one">
          <div class="services__head">Interpretações</div>
          <div class="services__sub">Análise Vocacional</div>
        </div>
        <div class="services__col services__col--two">
          <div class="services__head">Tendências</div>
          <div class="services__sub">Relacionamentos</div>
        </div>
        <div class="services__col services__col--three">
          <div class="services__head">Autoconhecimento</div>
          <div class="services__sub">Direcionamento de Carreira</div>
          <div class="services__sub services__sub--large">Astrologia Empresarial</div>
        </div>
      </div>
      <div class="services__floral">Terapia Floral <span>– Florias de Dorsk e Rui Tavenco</span></div>
    </div>
  </section>

</body>
</html>
```